Industrial & commercial facility maintenance flyer

Design a 2 sided flyer that outlines our core business unit services. One side shall be for our industrial maintenance division while the other will be focused on our commercial maintenance division.

Media from website here: https://files.vornelbox.net/share/7Kq29XzPw4RtLmYc8NdHe5JbVa

Target Market(s)

Industrial and commercial facility maintenance companies and professionals

Industry/Entity Type

Maintenance

Font styles to use
Serif

Colors
ffffff
2f73b4
0455a3
cfdfed

Requirements
Must have
• Several photos of each applicable service. Reference existing website (www.trelcorp.com). Use of the blue and grey scheme of our current logo.
Nice to have
• Our logo design across the top with our contact information on the bottom.

```html
<!DOCTYPE html>
<html lang="en">
<head>
<meta charset="utf-8">
<title>Halvern Maintenance Solutions – Flyer</title>
<link rel="stylesheet" href="https://fonts.googleapis.com/css2?family=Oswald:wght@500;600&family=Roboto:wght@300;500&display=swap">
<style>
  :root{
    --blue-deep:#1f4f99;
    --blue:#2d6db5;
    --blue-light:#4a90d0;
    --blue-pale:#cfdfed;
    --grey-dark:#536270;
    --grey:#8a959f;
    --grey-light:#c9cfd5;
    --ink:#222;
    --page:#eef0f2;
    --white:#ffffff;
  }
  *{margin:0;padding:0;box-sizing:border-box}
  html,body{width:1200px;height:722px;overflow:hidden;background:var(--page)}
  .spread{position:relative;width:1200px;height:722px}
  .flyer-frame{position:absolute;top:50px;width:570px;height:622px;overflow:hidden;box-shadow:0 2px 6px rgba(0,0,0,.25);background:var(--white)}
  .flyer-frame.industrial{left:20px}
  .flyer-frame.commercial{left:610px}
  .flyer{position:absolute;top:0;left:0;width:612px;height:668px;transform:scale(.9314);transform-origin:0 0}
  .flyer-art{position:absolute;inset:0;width:612px;height:668px}
  .brand{position:absolute;top:40px;left:0;width:612px;display:flex;justify-content:center;align-items:center;gap:10px}
  .brand-mark{width:46px;height:46px;border-radius:50%;background:var(--blue-deep)}
  .brand-name{font-family:"Roboto",sans-serif;font-weight:500;font-size:19px;color:var(--blue-deep);letter-spacing:.2px}
  .title-band{position:absolute;top:140px;height:57px;display:flex;align-items:center;font-family:"Oswald",sans-serif;font-weight:600;font-size:29px;color:var(--white);letter-spacing:.2px}
  .industrial .title-band{left:97px;width:515px;background:var(--blue-deep);padding-left:23px}
  .commercial .title-band{left:0;width:509px;background:var(--grey);justify-content:flex-end;padding-right:14px}
  .intro{position:absolute;top:221px;font-family:"Roboto",sans-serif;font-weight:300;font-size:10.2px;line-height:15px;color:var(--ink);text-align:justify}
  .industrial .intro{left:120px;width:362px}
  .commercial .intro{left:126px;width:362px}
  .url-band{position:absolute;top:407px;height:41px;display:flex;align-items:center;justify-content:center;font-family:"Oswald",sans-serif;font-weight:600;font-size:20px;color:var(--white)}
  .industrial .url-band{left:0;width:252px;background:var(--blue);padding-left:80px}
  .commercial .url-band{left:361px;width:251px;background:var(--grey-dark);padding-right:30px}
</style>
</head>
<body>
<main class="spread">

  <section class="flyer-frame industrial">
    <div class="flyer">
      <svg class="flyer-art" viewBox="0 0 612 668" aria-hidden="false">
        <defs>
          <linearGradient id="photoSteel" x1="0" y1="0" x2="1" y2="1"><stop offset="0" stop-color="#8fa3b8"/><stop offset="1" stop-color="#d2b46a"/></linearGradient>
          <linearGradient id="photoWorker" x1="0" y1="0" x2="1" y2="1"><stop offset="0" stop-color="#c6d2de"/><stop offset="1" stop-color="#2b4a86"/></linearGradient>
          <linearGradient id="photoHands" x1="0" y1="0" x2="1" y2="1"><stop offset="0" stop-color="#b9d4ee"/><stop offset="1" stop-color="#e8c89a"/></linearGradient>
          <linearGradient id="photoFactory" x1="0" y1="0" x2="0" y2="1"><stop offset="0" stop-color="#9aa6b0"/><stop offset="1" stop-color="#6d6a58"/></linearGradient>
        </defs>
        <polygon points="0,0 140,0 0,148" fill="var(--blue-light)"/>
        <polygon points="0,0 92,0 0,110" fill="var(--blue-deep)"/>
        <polygon points="612,305 612,668 380,668" fill="var(--blue-deep)"/>
        <polygon points="0,600 360,580 612,560 612,668 0,668" fill="var(--blue)"/>
        <polygon points="170,668 612,575 612,668" fill="var(--blue-deep)"/>

        <circle cx="390" cy="425" r="60" fill="none" stroke="var(--blue-deep)" stroke-width="24" stroke-dasharray="18 13"/>
        <circle cx="390" cy="425" r="65" fill="var(--blue-deep)"/>
        <circle cx="390" cy="425" r="54" fill="url(#photoSteel)" role="img" aria-label="Photo: steel plant production floor"/>

        <circle cx="545" cy="405" r="66" fill="none" stroke="var(--grey-light)" stroke-width="24" stroke-dasharray="19 14"/>
        <circle cx="545" cy="405" r="70" fill="var(--grey-light)"/>
        <circle cx="545" cy="405" r="60" fill="url(#photoWorker)" role="img" aria-label="Photo: technician in gloves tightening a valve"/>

        <circle cx="315" cy="590" r="66" fill="none" stroke="var(--blue-light)" stroke-width="24" stroke-dasharray="19 14"/>
        <circle cx="315" cy="590" r="70" fill="var(--blue-light)"/>
        <circle cx="315" cy="590" r="60" fill="url(#photoHands)" role="img" aria-label="Photo: handshake over plans with a hard hat"/>

        <circle cx="495" cy="592" r="86" fill="none" stroke="var(--white)" stroke-width="24" stroke-dasharray="22 16"/>
        <circle cx="495" cy="592" r="90" fill="var(--white)"/>
        <circle cx="495" cy="592" r="80" fill="url(#photoFactory)" role="img" aria-label="Photo: large factory assembly hall"/>
      </svg>

      <div class="brand"><span class="brand-mark"></span><span class="brand-name">Halvern Maintenance Solutions</span></div>
      <h1 class="title-band">Industrial Maintenance Solutions</h1>
      <p class="intro">Our industrial maintenance teams work in the field to handle your needs as quickly as possible, whether to get your critical broken or malfunctioning equipment going again or to support scheduled downtime. We specialize in industrial maintenance, conveyer repair, and overhead door repair, but our industrial services aren't limited to those services. Others include equipment repairs, installation, and adjustment, just to name a few.</p>
      <div class="url-band">www.trelcorp.com</div>
    </div>
  </section>

  <section class="flyer-frame commercial">
    <div class="flyer">
      <svg class="flyer-art" viewBox="0 0 612 668">
        <defs>
          <linearGradient id="photoTower" x1="0" y1="0" x2="0" y2="1"><stop offset="0" stop-color="#a9c4e2"/><stop offset="1" stop-color="#3c4a5a"/></linearGradient>
          <linearGradient id="photoInspect" x1="0" y1="0" x2="1" y2="1"><stop offset="0" stop-color="#e4e8ec"/><stop offset="1" stop-color="#2a3f72"/></linearGradient>
          <linearGradient id="photoTech" x1="0" y1="0" x2="1" y2="1"><stop offset="0" stop-color="#dadcd8"/><stop offset="1" stop-color="#2e4a8a"/></linearGradient>
          <linearGradient id="photoStore" x1="0" y1="0" x2="0" y2="1"><stop offset="0" stop-color="#6d8db8"/><stop offset="1" stop-color="#b0663c"/></linearGradient>
        </defs>
        <polygon points="470,0 612,0 612,148" fill="var(--grey)"/>
        <polygon points="515,0 612,0 612,112" fill="var(--grey-dark)"/>
        <polygon points="0,300 0,668 230,668" fill="var(--blue-deep)"/>
        <polygon points="180,600 360,570 612,605 612,668 120,668" fill="var(--blue)"/>

        <circle cx="55" cy="395" r="66" fill="none" stroke="var(--blue-light)" stroke-width="24" stroke-dasharray="19 14"/>
        <circle cx="55" cy="395" r="70" fill="var(--blue-light)"/>
        <circle cx="55" cy="395" r="60" fill="url(#photoTower)" role="img" aria-label="Photo: office tower seen from below"/>

        <circle cx="210" cy="420" r="62" fill="none" stroke="var(--blue-deep)" stroke-width="24" stroke-dasharray="18 13"/>
        <circle cx="210" cy="420" r="66" fill="var(--blue-deep)"/>
        <circle cx="210" cy="420" r="56" fill="url(#photoInspect)" role="img" aria-label="Photo: technician inspecting a sink with a clipboard"/>

        <circle cx="92" cy="585" r="86" fill="none" stroke="var(--grey-light)" stroke-width="24" stroke-dasharray="22 16"/>
        <circle cx="92" cy="585" r="90" fill="var(--grey-light)"/>
        <circle cx="92" cy="585" r="80" fill="url(#photoTech)" role="img" aria-label="Photo: service technician carrying a toolbox"/>

        <circle cx="295" cy="562" r="64" fill="none" stroke="var(--blue-light)" stroke-width="24" stroke-dasharray="19 14"/>
        <circle cx="295" cy="562" r="68" fill="var(--blue-light)"/>
        <circle cx="295" cy="562" r="58" fill="url(#photoStore)" role="img" aria-label="Photo: retail building at dusk"/>
      </svg>

      <div class="brand"><span class="brand-mark"></span><span class="brand-name">Halvern Maintenance Solutions</span></div>
      <h1 class="title-band">Commercial Maintenance Solutions</h1>
      <p class="intro">Halvern Maintenance Solutions knows how important it is to convert window shoppers to paying customers and to move inventory off your shelves. We ensure that your business is always looking its best with our cost-effective maintenance programs and crews available 24/7 to take care of any equipment or facility malfunction as quickly as possible.</p>
      <div class="url-band">www.trelcorp.com</div>
    </div>
  </section>

</main>
</body>
</html>
```